Kestrel.vc needs a better website design!

We need a new and better website for Kestrel.vc. We're a Canadian venture capital firm that invests in innovative entrepreneurs. We compete against the following websites: lumora.vc, brightvalefund.ca, osprovc.com, and tessara.vc. We're a diverse group of partners and we're dedicated to the founders we invest in.
Updates

I don’t really like stock photos of random people as part of the website design…so please try to stay away from using those images. Thanks, Owen

Target Market(s)

Canadian entrepreneurs and investors

Industry/Entity Type

Venture capital, finance, investment, entrepreneurship

Coding

Coded - Design and coding required

Number of Pages Required

4 page

Font styles to use
Sans Serif

Colors

Designer to choose colors to be used in the design.

Requirements
Must have
• Clean crisp overall design. Fast and to the point.
Nice to have
• Check out www.kestrel.vc - I did it myself and it is too basic and too wordy.
Should not have
• No stock images with random people in them! Not too wordy or with too many large images that are slow to load.

```html
<!DOCTYPE html>
<html lang="en">
<head>
<meta charset="utf-8">
<title>Kestrel.vc — Venture Capital</title>
<link href="https://fonts.googleapis.com/css2?family=Manrope:wght@400;500;600;700;800&display=swap" rel="stylesheet">
<style>
:root{
  --backdrop:#d7e0cc;
  --white:#ffffff;
  --tint:#f3f6ec;
  --ink:#2b2b2b;
  --text:#3a3a3a;
  --muted:#5c5c5c;
  --green:#8aa238;
  --green-dark:#6c8428;
  --footer-top:#2e2e2e;
  --footer-bottom:#151515;
  --shadow:0 6px 22px rgba(60,80,30,.08);
}
*{box-sizing:border-box;margin:0;padding:0}
html,body{width:1200px;height:2405px;overflow:hidden;background:var(--backdrop);font-family:'Manrope',sans-serif;color:var(--ink)}
.page{position:absolute;left:51px;top:50px;width:1098px;height:2320px;background:var(--white);border-radius:28px;overflow:hidden}
.abs{position:absolute}
a{color:inherit;text-decoration:none}

/* header */
.brand{left:58px;top:27px;display:flex;align-items:center;gap:10px;font-weight:700;font-size:20px;color:var(--green-dark)}
.brand-dot{width:30px;height:30px;border-radius:50%;background:var(--green)}
.nav{left:496px;top:40px;display:flex;gap:33px;font-size:16px;font-weight:500;color:var(--ink)}
.call-btn{left:911px;top:28px;width:130px;height:43px;border-radius:22px;background:var(--ink);color:#fff;display:flex;align-items:center;justify-content:center;gap:8px;font-size:16px;font-weight:500}

/* hero */
.hero-bg{left:0;top:500px;width:1098px;height:900px;background:var(--tint)}
.hero-curve{left:0;top:510px}
.hero-title{left:82px;top:178px;font-size:54px;line-height:57px;font-weight:700;letter-spacing:-1.5px;color:var(--ink)}
.hero-title span{color:var(--green)}
.hero-text{left:82px;top:314px;width:460px;font-size:16px;line-height:25px;color:var(--text)}
.btn-dark{left:82px;top:424px;width:164px;height:57px;background:var(--ink);color:#fff;border-radius:4px;display:flex;align-items:center;justify-content:center;gap:14px;font-size:16px;font-weight:500}
.hero-art{left:597px;top:137px;width:406px;height:363px;border-radius:48% 52% 40% 44%/50% 46% 54% 50%;background:radial-gradient(circle at 55% 55%,#dfe9c6 0%,#e8efd8 45%,#f6f8f0 75%,rgba(255,255,255,0) 100%)}

/* features */
.feature{height:137px;background:#fff;border-radius:10px;box-shadow:var(--shadow);display:flex;align-items:center;padding:0 25px;gap:18px}
.feature-avatar{width:96px;height:96px;border-radius:50%;flex:none}
.feature p{font-size:16px;line-height:25px;color:var(--muted)}

/* portfolio */
.section-title{width:1098px;left:0;text-align:center;font-size:30px;line-height:31px;font-weight:400;letter-spacing:-.5px;color:var(--ink)}
.logo-cell{width:237px;height:96px;background:#fff;border-radius:8px;box-shadow:var(--shadow);display:flex;align-items:center;justify-content:center;gap:8px;font-size:22px;font-weight:700;color:var(--ink)}
.logo-cell .mark{width:16px;height:16px;border-radius:50%}
.logo-cell.open{height:245px;flex-direction:column;align-items:flex-start;justify-content:flex-start;padding:24px 27px 0}
.open .open-head{align-self:center;display:flex;align-items:center;gap:8px;font-size:26px;font-weight:500;color:#333}
.open p{margin-top:22px;font-size:16px;line-height:25px;font-weight:400;color:var(--muted)}
.read-more{display:flex;align-items:center;gap:10px;font-size:16px;font-weight:500;color:var(--green)}
.underline-link{display:flex;align-items:center;gap:12px;font-size:16px;font-weight:500;color:var(--ink)}
.underline-link span{border-bottom:1.5px solid currentColor;padding-bottom:2px}

/* contact band */
.contact-band{left:0;top:1324px;width:1098px;height:210px;background:linear-gradient(90deg,#89a135 0%,#7e9832 55%,#6b8129 100%)}
.contact-band h2{position:absolute;top:52px;width:100%;text-align:center;font-size:30px;line-height:31px;font-weight:400;color:#fff;letter-spacing:-.5px}
.contact-band .underline-link{position:absolute;left:497px;top:146px;color:#fff}

/* news */
.news-card{width:317px;height:330px;background:#fff;border-radius:12px;box-shadow:0 6px 24px rgba(0,0,0,.07);padding:24px 23px}
.news-img{width:270px;height:148px}
.news-card p{margin-top:28px;font-size:16px;line-height:25px;color:var(--muted)}
.news-card .read-more{margin-top:18px}

/* footer */
.footer{left:0;top:2058px;width:1098px;height:262px;background:linear-gradient(180deg,var(--footer-top),var(--footer-bottom))}
.footer-brand{position:absolute;top:42px;left:0;width:100%;display:flex;justify-content:center;align-items:center;gap:12px;font-size:24px;font-weight:600;color:#fff}
.footer-brand .brand-dot{width:52px;height:52px;background:none;border:2.5px solid #fff}
.footer-nav{position:absolute;top:138px;left:0;width:100%;display:flex;justify-content:center;gap:33px;font-size:16px;font-weight:500;color:#fff}
.copyright{position:absolute;top:204px;left:0;width:100%;text-align:center;font-size:15px;color:#9a9a9a}
</style>
</head>
<body>
<div class="page">

  <div class="abs hero-bg"></div>
  <svg class="abs hero-curve" width="1098" height="120" viewBox="0 0 1098 120" aria-hidden="true">
    <path d="M0 0 H1098 V0 C900 60 700 100 0 122 Z" fill="#fff"/>
    <path d="M0 122 C700 100 900 60 1098 0 V120 H0 Z" fill="var(--tint)"/>
  </svg>

  <header>
    <a class="abs brand" href="#"><span class="brand-dot"></span>Kestrel.vc</a>
    <nav class="abs nav">
      <a href="#">People</a><a href="#">We Look For</a><a href="#">Companies</a><a href="#">About us</a>
    </nav>
    <a class="abs call-btn" href="#">
      <svg width="18" height="18" viewBox="0 0 24 24" fill="none" stroke="#fff" stroke-width="1.8" stroke-linecap="round" stroke-linejoin="round"><path d="M22 16.9v3a2 2 0 0 1-2.2 2 19.8 19.8 0 0 1-8.6-3.1 19.5 19.5 0 0 1-6-6A19.8 19.8 0 0 1 2.1 4.2 2 2 0 0 1 4.1 2h3a2 2 0 0 1 2 1.7c.1.9.4 1.8.7 2.7a2 2 0 0 1-.5 2.1L8 9.8a16 16 0 0 0 6 6l1.3-1.3a2 2 0 0 1 2.1-.4c.9.3 1.8.6 2.7.7a2 2 0 0 1 1.7 2z"/></svg>
      Call Now
    </a>
  </header>

  <section class="hero">
    <h1 class="abs hero-title">United we are<br>stronger, <span>the better</span></h1>
    <p class="abs hero-text">We are a venture capital firm who invest in innovative seed-stage technology companies in Western Canada focused on B2B and SaaS markets.</p>
    <a class="abs btn-dark" href="#">Learn More
      <svg width="9" height="14" viewBox="0 0 9 14" fill="none" stroke="#fff" stroke-width="1.8"><path d="M1.5 1.5 7 7l-5.5 5.5"/></svg>
    </a>
    <div class="abs hero-art" role="img" aria-label="Illustration of a businessman with a briefcase running up a rising orange growth arrow among plants, clouds and gears"></div>
  </section>

  <section class="features">
    <div class="abs feature" style="left:138px;top:561px;width:396px">
      <div class="feature-avatar" role="img" aria-label="Illustration of a woman presenting a bar chart" style="background:linear-gradient(135deg,#bfe4d3,#e9a23b)"></div>
      <p>Mentoring and strategic advice to help you grow your company quickly and efficiently</p>
    </div>
    <div class="abs feature" style="left:555px;top:561px;width:404px">
      <div class="feature-avatar" role="img" aria-label="Illustration of a woman in front of a world map with message icons" style="background:linear-gradient(135deg,#8fd3cb,#5bb8b0)"></div>
      <p>Mentoring and strategic advice to help you grow your company quickly and efficiently</p>
    </div>
  </section>

  <section class="portfolio">
    <h2 class="abs section-title" style="top:800px">Let’s show you some of our<br>innovative portfolio companies</h2>

    <div class="abs logo-cell" style="left:58px;top:904px"><span class="mark" style="background:var(--green)"></span>Sparkline</div>
    <div class="abs logo-cell" style="left:306px;top:904px;font-weight:500;color:#6aa39a">Tidewell</div>
    <div class="abs logo-cell" style="left:554px;top:904px;font-weight:800">Questory</div>
    <div class="abs logo-cell" style="left:803px;top:904px;font-weight:500">Keyfold</div>

    <div class="abs logo-cell" style="left:58px;top:1011px;font-weight:800">Opsbridge</div>
    <div class="abs logo-cell open" style="left:306px;top:1011px">
      <div class="open-head">Homely<span class="mark" style="width:26px;height:26px;border-radius:50%;background:#a7dcc5"></span></div>
      <p>Homely is an intuitive, secure and private mortgage application platform...</p>
      <a class="read-more" href="#" style="align-self:center;margin-top:27px">Read More
        <svg width="8" height="13" viewBox="0 0 8 13" fill="none" stroke="currentColor" stroke-width="1.8"><path d="M1.5 1.5 6.5 6.5l-5 5"/></svg></a>
    </div>
    <div class="abs logo-cell" style="left:554px;top:1011px;font-size:17px;font-weight:600;letter-spacing:1px">Ledgerly</div>
    <div class="abs logo-cell" style="left:803px;top:1011px;font-weight:700">Nutrisync</div>

    <a class="abs underline-link" href="#" style="left:963px;top:1224px">
      <span>View All</span>
      <svg width="8" height="13" viewBox="0 0 8 13" fill="none" stroke="currentColor" stroke-width="1.8"><path d="M1.5 1.5 6.5 6.5l-5 5"/></svg>
    </a>
  </section>

  <section class="abs contact-band">
    <h2>Contact us today if you have<br>what we’re looking for</h2>
    <a class="underline-link" href="#"><span>Contact us</span>
      <svg width="8" height="13" viewBox="0 0 8 13" fill="none" stroke="currentColor" stroke-width="1.8"><path d="M1.5 1.5 6.5 6.5l-5 5"/></svg></a>
  </section>

  <section class="news">
    <h2 class="abs section-title" style="top:1610px">Latest News</h2>
    <a class="abs underline-link" href="#" style="left:943px;top:1640px"><span>View More</span>
      <svg width="8" height="13" viewBox="0 0 8 13" fill="none" stroke="currentColor" stroke-width="1.8"><path d="M1.5 1.5 6.5 6.5l-5 5"/></svg></a>

    <article class="abs news-card" style="left:58px;top:1685px">
      <div class="news-img" role="img" aria-label="News photo of a presenter beside an avatar by a lakeside fire pit" style="background:linear-gradient(135deg,#9aa7a0,#3b3a36 70%,#c8842c)"></div>
      <p>Lorem ipsum dolor sit amet, consectetur adipiscing elit, sed do eiusmod tempor incididunt ut</p>
      <a class="read-more" href="#">Read More <svg width="8" height="13" viewBox="0 0 8 13" fill="none" stroke="currentColor" stroke-width="1.8"><path d="M1.5 1.5 6.5 6.5l-5 5"/></svg></a>
    </article>
    <article class="abs news-card" style="left:390px;top:1685px">
      <div class="news-img" role="img" aria-label="News photo of a hand refuelling a red car with a green fuel nozzle" style="background:linear-gradient(135deg,#7d1515,#2c2a28 55%,#2f7a3a)"></div>
      <p>Lorem ipsum dolor sit amet, consectetur adipiscing elit, sed do eiusmod tempor incididunt ut</p>
      <a class="read-more" href="#">Read More <svg width="8" height="13" viewBox="0 0 8 13" fill="none" stroke="currentColor" stroke-width="1.8"><path d="M1.5 1.5 6.5 6.5l-5 5"/></svg></a>
    </article>
    <article class="abs news-card" style="left:723px;top:1685px">
      <div class="news-img" role="img" aria-label="News photo of a speaker at a podium at a conference" style="background:linear-gradient(135deg,#1c3c8a,#2b56b0 50%,#d9c02a)"></div>
      <p>Lorem ipsum dolor sit amet, consectetur adipiscing elit, sed do eiusmod tempor incididunt ut</p>
      <a class="read-more" href="#">Read More <svg width="8" height="13" viewBox="0 0 8 13" fill="none" stroke="currentColor" stroke-width="1.8"><path d="M1.5 1.5 6.5 6.5l-5 5"/></svg></a>
    </article>
  </section>

  <footer class="abs footer">
    <div class="footer-brand"><span class="brand-dot"></span>KESTREL.VC</div>
    <nav class="footer-nav">
      <a href="#">People</a><a href="#">We Look For</a><a href="#">Companies</a><a href="#">About us</a><a href="#">Call Now</a>
    </nav>
    <p class="copyright">Copyright © 2021 Kestrel.vc - All Rights Reserved</p>
  </footer>

</div>
</body>
</html>
```